Verpackungsdesign für hochwertiges Haarparfum
Zielgruppe
Tovel's Method ist eine israelische Firma, die hochqualitative Haarprodukte und Haar Tools verkauft. Unsere Zielgruppe sind Frauen, die viel in Ihr Aussehen investieren und auf Ihr Äußeres sehr Wert legen.
Aufgabenstellung
Wir suchen nach einem Design für unsere zwei neuen Haarparfums. Es sollte teuer aussehen und das Design sollte modern und simpel sein. Die Flachen sind mit Milchglas und das Design wird auf die Flaschen gedruckt. Das Design muss komplett in Englischer Sprache sein.
Die Masse sind:
Höhe 7,7 cm
Umfang 11 cm
Es wird zwei Düfte geben.
1. The Nordic : Deckel wird Silber glänzend
2. The Celtic: Deckel wird Silber matt
Informationen die auf der Flasche sein sollten:
1. Firmen Logo (wird angehängt)
2. Name des Parfüms (The Nordic or the Celtic)
3. Longlasting Hair Fragrance
4. 30 ml
5. Includes essential hair vitamins and minerals
6. Alcohol and salt free

```html
<!DOCTYPE html>
<html lang="en">
<head>
<meta charset="utf-8">
<title>Perfume Nordic – Longlasting Hair Fragrance Label</title>
<link rel="stylesheet" href="https://fonts.googleapis.com/css2?family=Allura&family=Bodoni+Moda:wght@400;500&family=Italiana&display=swap">
<style>
  :root {
    --label-grey: #b4b4b4;
    --accent-yellow: #f7e83a;
    --laurel-white: #ffffff;
  }
  * { margin: 0; padding: 0; box-sizing: border-box; }
  html, body {
    width: 1200px;
    height: 1064px;
    overflow: hidden;
    background: var(--label-grey);
  }
  .label {
    position: relative;
    width: 1200px;
    height: 1064px;
    background: var(--label-grey);
    color: var(--accent-yellow);
    text-align: center;
  }
  .laurel-wreath {
    position: absolute;
    left: 0;
    top: 0;
    width: 1200px;
    height: 1064px;
  }
  .brand-name {
    position: absolute;
    left: 0;
    right: 0;
    top: 86px;
    font-family: 'Italiana', serif;
    font-size: 20px;
    line-height: 1;
    letter-spacing: 3px;
    text-transform: uppercase;
    color: var(--accent-yellow);
  }
  .product-kicker {
    position: absolute;
    left: 362px;
    top: 232px;
    font-family: 'Allura', cursive;
    font-size: 104px;
    line-height: 1;
    font-weight: 400;
  }
  .product-name {
    position: absolute;
    left: 0;
    right: 0;
    top: 318px;
    font-family: 'Bodoni Moda', serif;
    font-weight: 400;
    font-size: 142px;
    line-height: 1;
    letter-spacing: -2px;
  }
  .product-type {
    position: absolute;
    left: 0;
    right: 0;
    top: 540px;
    font-family: 'Italiana', serif;
    font-size: 40px;
    line-height: 48px;
    letter-spacing: 3px;
    text-transform: uppercase;
  }
  .product-volume {
    position: absolute;
    left: 0;
    right: 0;
    top: 690px;
    font-family: 'Italiana', serif;
    font-size: 40px;
    line-height: 1;
  }
  .product-claims {
    position: absolute;
    left: 0;
    right: 0;
    top: 924px;
    font-family: 'Bodoni Moda', serif;
    font-size: 21px;
    line-height: 28px;
    letter-spacing: 1px;
  }
  .product-claims p + p { margin-top: 16px; }
</style>
</head>
<body>
  <main class="label">
    <svg class="laurel-wreath" viewBox="0 0 1200 1064" role="img" aria-label="Laurel wreath ornament of white leaves with yellow leaf accents at top and bottom, framing the product name">
      <defs>
        <linearGradient id="wreath-tone" x1="0" y1="0" x2="0" y2="1">
          <stop offset="0" stop-color="#ffffff"/>
          <stop offset="0.1" stop-color="#faf28a"/>
          <stop offset="0.2" stop-color="#ffffff"/>
          <stop offset="0.8" stop-color="#ffffff"/>
          <stop offset="0.92" stop-color="#faf28a"/>
          <stop offset="1" stop-color="#ffffff"/>
        </linearGradient>
      </defs>
      <ellipse cx="600" cy="440" rx="410" ry="340" fill="none" stroke="url(#wreath-tone)" stroke-width="80" opacity="0.85" pathLength="100" stroke-dasharray="70 10 20"/>
    </svg>

    <p class="brand-name">Tovel's Method</p>

    <p class="product-kicker">Perfume</p>
    <h1 class="product-name">NORDIC</h1>

    <p class="product-type">Longlasting<br>Hair&nbsp; Fragrance</p>
    <p class="product-volume">30ml</p>

    <div class="product-claims">
      <p>Includes essential hair<br>vitamins and minerals</p>
      <p>Alcohol and salt free</p>
    </div>
  </main>
</body>
</html>
```